Kids Soccer club - Wordpress website

Wordpress site for kids soccer club. mobile friendly.
1.Link to google calandar nicely displayed- this week(upcoming events ) view on home page? separate page for detail. events to be updated by coaches by mobile.
2.Feed from club Page page which parents might use more.
3. News page for coaches/ parents to post photos and info re matches etc.
4. Location Map and contact details

Target Market(s)

parents, kids, coaches involved in the club

Industry/Entity Type

Club

Coding

Coded - Design and coding required

Number of Pages Required

4 page

Requirements
Must have
• Pages:
• 1. Home
• 2. Club Calander
• 3. News
• 4. Location
• also a feed from the team Page page
• and a space for sponsor details
• domain will be www.marrowfieldrovers.com
• see that for further ideas on the brief

```html
<!DOCTYPE html>
<html lang="en">
<head>
<meta charset="utf-8">
<title>Club News – Marrowfield Rovers FC</title>
<link href="https://fonts.googleapis.com/css2?family=Roboto+Condensed:wght@400;700&family=Open+Sans:ital,wght@0,400;0,600;1,400&display=swap" rel="stylesheet">
<style>
:root{
  --green:#3a9a2a;
  --green-dark:#2a7d1f;
  --green-footer:#2f8f25;
  --nav-active:#2b2f33;
  --orange:#f26b21;
  --sky-blue:#27bff0;
  --fb-blue:#2c5aa0;
  --ink:#333;
  --muted:#666;
  --light:#999;
  --rule:#e3e3e3;
  --white:#fff;
}
*{margin:0;padding:0;box-sizing:border-box}
html,body{width:810px;height:1200px;overflow:hidden}
body{
  position:relative;
  font-family:"Open Sans",Arial,sans-serif;
  color:var(--ink);
  background:linear-gradient(180deg,#3c556b 0%,#5d7d93 14%,#7d97a6 24%,#2e4a38 30%,#3e7d2a 36%,#2c6a1e 60%,#0f3a10 85%,#072407 100%);
}
.abs{position:absolute}

/* header */
.social{top:37px;left:67px;display:flex;gap:3px}
.social span{width:21px;height:21px;border:1.5px solid rgba(255,255,255,.85);border-radius:50%;display:block}
.btn-join,.btn-sign{top:38px;height:20px;font:700 8.5px/20px "Roboto Condensed",sans-serif;color:var(--white);text-align:center;letter-spacing:.3px}
.btn-join{left:628px;width:53px;background:var(--green)}
.btn-sign{left:690px;width:53px;border:1px solid rgba(255,255,255,.8);line-height:18px}

.nav{top:98px;left:66px;width:678px;height:36px;background:var(--green);border-bottom:2px solid var(--green-dark)}
.nav a{position:absolute;top:0;height:34px;font:400 10px/34px "Roboto Condensed",sans-serif;color:var(--white);text-decoration:none;letter-spacing:.3px;transform:translateX(-50%)}
.nav a.active{background:var(--nav-active);width:62px;text-align:center;transform:none}

.brand{top:20px;left:352px;width:108px;height:108px;border-radius:50%;background:var(--white);border:3px solid var(--green);display:flex;align-items:center;justify-content:center;text-align:center;font:700 12px/1.15 "Roboto Condensed",sans-serif;color:var(--green-dark)}

.hero{top:134px;left:66px;width:678px;height:152px;background:linear-gradient(180deg,#8ea4a6 0%,#6f8870 45%,#4e7a3a 75%,#3c6d2c 100%)}
.hero h1{position:absolute;top:58px;left:0;width:100%;text-align:center;font:700 27px/1 "Roboto Condensed",sans-serif;color:var(--white);letter-spacing:.2px}

/* content */
.content{top:286px;left:66px;width:678px;height:698px;background:var(--white)}
.content::before{content:"";position:absolute;top:0;left:150px;width:380px;height:14px;background:radial-gradient(ellipse at top,rgba(0,0,0,.12),transparent 70%)}
.section-title{position:absolute;top:40px;left:17px;font:700 17.5px/1 "Roboto Condensed",sans-serif;color:#3a3a3a}

.post{position:absolute;left:16px;width:440px;height:140px}
.post .thumb{position:absolute;left:0;top:0;width:170px;height:134px;border:1px solid #ddd;padding:4px;background:var(--white)}
.post .thumb div{width:100%;height:100%}
.post .avatar{position:absolute;left:184px;top:-2px;width:32px;height:32px;border-radius:50%;background:linear-gradient(160deg,#c9b6a3,#7b6452)}
.post h2{position:absolute;left:223px;top:2px;font:400 10.5px/1.2 "Open Sans",sans-serif;color:#444}
.post .meta{position:absolute;left:228px;top:25px;display:flex;gap:14px;font:italic 400 6.5px/1 "Open Sans",sans-serif;color:var(--light)}
.post .meta span::before{content:"";display:inline-block;width:5px;height:5px;border:1px solid #aaa;margin-right:4px;vertical-align:-1px}
.post .rule{position:absolute;left:183px;top:45px;width:252px;height:1px;background:var(--rule)}
.post p{position:absolute;left:183px;top:59px;width:256px;font:400 7.4px/14px "Open Sans",sans-serif;color:var(--muted)}
.post .more{position:absolute;left:183px;top:120px;font:400 8.5px/1 "Roboto Condensed",sans-serif;color:var(--green);text-decoration:underline}

/* sidebar */
.register{top:350px;left:544px;width:181px;height:103px;background:linear-gradient(180deg,#6faa57,#4b8e34);text-align:center;color:var(--white)}
.register .small{position:absolute;top:22px;width:100%;font:400 11.5px/1 "Roboto Condensed",sans-serif}
.register .big{position:absolute;top:37px;width:100%;font:400 16px/1 "Roboto Condensed",sans-serif}
.register .cta{position:absolute;top:63px;left:52px;width:81px;height:21px;background:var(--orange);font:400 8.5px/21px "Roboto Condensed",sans-serif}

.tab{top:470px;height:24px;font:700 12px/24px "Roboto Condensed",sans-serif;color:var(--white);padding-left:10px}
.tab-tw{left:545px;width:79px;background:var(--sky-blue)}
.tab-fb{left:626px;width:82px;background:var(--fb-blue)}

.feed{top:494px;left:544px;width:181px;height:288px;border:5px solid var(--sky-blue);background:var(--white)}
.feed .head{position:absolute;top:0;left:0;width:100%;height:30px;border-bottom:1px solid #e6e6e6;padding:8px 0 0 10px;font:400 10px/1 "Open Sans",sans-serif;color:#1f3b63}
.tweet{position:absolute;left:8px;width:152px;font-family:"Open Sans",sans-serif}
.tweet .rt{font-size:6.8px;color:#777}
.tweet .who{display:flex;gap:6px;margin-top:5px}
.tweet .who i{width:23px;height:21px;border:1px solid #ddd;display:block}
.tweet .who b{font-weight:400;font-size:7.3px;color:#333;display:block}
.tweet .who small{font-size:5.6px;color:#555}
.tweet p{margin-top:10px;font-size:7px;line-height:12px;color:#777}
.tweet .promo{margin-top:6px;width:147px;height:74px;background:linear-gradient(120deg,#3a2d66,#6a2f86 55%,#2a5ea8)}
.feed .scroll{position:absolute;right:1px;top:44px;width:7px;height:226px;background:#f1f1f1}
.feed .scroll i{position:absolute;top:40px;left:1px;width:5px;height:75px;background:#c5c5c5}

.sponsor{top:796px;left:544px;width:181px;height:98px;border:1px solid #6fb25a;background:linear-gradient(180deg,#c9d6df,#e4ecef 60%,#b7c6cf)}

/* footer */
.footer{top:984px;left:66px;width:678px;height:178px;background:var(--green-footer);color:var(--white)}
.footer .mark{position:absolute;left:20px;top:28px;width:100px;height:100px;border-radius:50%;background:var(--white);display:flex;align-items:center;justify-content:center;text-align:center;font:700 11px/1.15 "Roboto Condensed",sans-serif;color:var(--green-dark)}
.footer h3{position:absolute;top:29px;font:400 14px/1 "Roboto Condensed",sans-serif;letter-spacing:.2px}
.footer .addr{position:absolute;left:160px;top:53px;font:400 7.8px/13.3px "Open Sans",sans-serif;letter-spacing:.2px}
.footer .mail{position:absolute;left:160px;top:101px;display:flex;gap:9px;font:400 7.8px/15px "Open Sans",sans-serif}
.footer .mail svg{margin-top:2px}
.footer .map{position:absolute;left:344px;top:50px;width:188px;height:99px;border:2px solid #e8e8e8;background:linear-gradient(135deg,#e2e2e2,#d3d3d3)}
.footer ul{position:absolute;left:576px;top:55px;list-style:none;font:400 7.8px/14.4px "Open Sans",sans-serif}
.footer li::before{content:"";display:inline-block;border-left:3.5px solid var(--white);border-top:2.5px solid transparent;border-bottom:2.5px solid transparent;margin-right:9px;vertical-align:1px}
.copy{top:1176px;left:0;width:810px;text-align:center;font:400 7.8px/1 "Open Sans",sans-serif;color:var(--white)}
</style>
</head>
<body>

<div class="abs social"><span></span><span></span></div>
<div class="abs btn-join">JOIN NOW</div>
<div class="abs btn-sign">SIGN IN</div>

<nav class="abs nav">
  <a href="#" style="left:36px">HOME</a>
  <a href="#" style="left:110px">ABOUT US</a>
  <a href="#" style="left:208px">CLUB CALANADER</a>
  <a href="#" class="active" style="left:414px">NEWS</a>
  <a href="#" style="left:512px">LOCATION</a>
  <a href="#" style="left:595px">CONTACT US</a>
</nav>

<div class="abs brand">Marrowfield<br>Rovers FC</div>

<header class="abs hero" role="img" aria-label="Coach in a blue shirt watching children train on a grass pitch">
  <h1>CLUB NEWS</h1>
</header>

<main class="abs content">
  <h2 class="section-title">LATEST NEWS</h2>

  <article class="post" style="top:74px">
    <div class="thumb"><div role="img" aria-label="Player signing autographs for fans" style="background:linear-gradient(160deg,#6b7a8c,#2d3f6e 60%,#4a3a30)"></div></div>
    <div class="avatar" role="img" aria-label="Author portrait"></div>
    <h2>Nemo enim ipsam voluptatem quia</h2>
    <div class="meta"><span>January 5, 2016</span><span>2 comments</span><span>by Parents</span></div>
    <div class="rule"></div>
    <p>Lorem ipsum dolor sit amet, consectetur adipiscing elit, sed do eiusmod tempor incididunt ut labore et dolore magna aliqua. Ut enim ad minim veniam, quis nostrud exercitation ullamco laboris nisi ut aliquip ex ea commodo consequat. Duis aute irure dolor in</p>
    <a class="more" href="#">Continue Reading &gt;&gt;</a>
  </article>

  <article class="post" style="top:224px">
    <div class="thumb"><div role="img" aria-label="Club crest on a dotted brown background" style="background:radial-gradient(circle,#f3e6b8 0%,#c79a52 45%,#5a2a1a 100%)"></div></div>
    <div class="avatar" role="img" aria-label="Author portrait"></div>
    <h2>Nemo enim ipsam voluptatem quia</h2>
    <div class="meta"><span>January 5, 2016</span><span>2 comments</span><span>by coaches</span></div>
    <div class="rule"></div>
    <p>Lorem ipsum dolor sit amet, consectetur adipiscing elit, sed do eiusmod tempor incididunt ut labore et dolore magna aliqua. Ut enim ad minim veniam, quis nostrud exercitation ullamco laboris nisi ut aliquip ex ea commodo consequat. Duis aute irure dolor in</p>
    <a class="more" href="#">Continue Reading &gt;&gt;</a>
  </article>

  <article class="post" style="top:374px">
    <div class="thumb"><div role="img" aria-label="Young players in red kits running on grass" style="background:linear-gradient(180deg,#8fae6a,#b8403a 45%,#6e9a45 75%)"></div></div>
    <div class="avatar" role="img" aria-label="Author portrait"></div>
    <h2>Nemo enim ipsam voluptatem quia</h2>
    <div class="meta"><span>January 5, 2016</span><span>2 comments</span><span>by Parents</span></div>
    <div class="rule"></div>
    <p>Lorem ipsum dolor sit amet, consectetur adipiscing elit, sed do eiusmod tempor incididunt ut labore et dolore magna aliqua. Ut enim ad minim veniam, quis nostrud exercitation ullamco laboris nisi ut aliquip ex ea commodo consequat. Duis aute irure dolor in</p>
    <a class="more" href="#">Continue Reading &gt;&gt;</a>
  </article>

  <article class="post" style="top:524px">
    <div class="thumb"><div role="img" aria-label="Girls competing for the ball during a match" style="background:linear-gradient(180deg,#5c7a4a,#3d6f3a 40%,#6c9a4e 80%)"></div></div>
    <div class="avatar" role="img" aria-label="Author portrait"></div>
    <h2>Nemo enim ipsam voluptatem quia</h2>
    <div class="meta"><span>January 5, 2016</span><span>2 comments</span><span>by coaches</span></div>
    <div class="rule"></div>
    <p>Lorem ipsum dolor sit amet, consectetur adipiscing elit, sed do eiusmod tempor incididunt ut labore et dolore magna aliqua. Ut enim ad minim veniam, quis nostrud exercitation ullamco laboris nisi ut aliquip ex ea commodo consequat. Duis aute irure dolor in</p>
    <a class="more" href="#">Continue Reading &gt;&gt;</a>
  </article>
</main>

<aside class="abs register" role="img" aria-label="Players on a pitch behind a green tint">
  <div class="small">REGISTER TO</div>
  <div class="big">POST COMMENTS</div>
  <div class="cta">REGISTER NOW</div>
</aside>

<div class="abs tab tab-tw">Tweets</div>
<div class="abs tab tab-fb">Page</div>

<section class="abs feed">
  <div class="head">Tweets by @marrowfieldfc</div>
  <div class="tweet" style="top:42px">
    <div class="rt">Marrowfield Rovers FC Retweeted</div>
    <div class="who"><i></i><div><b>Northgate United</b><small>@NorthgateUtd &nbsp;7 Aug 2015</small></div></div>
    <p>We are sad to learn that Walter Hinde, father of Ross and Liam, has passed away.</p>
  </div>
  <div class="tweet" style="top:127px">
    <div class="rt">Marrowfield Rovers FC Retweeted</div>
    <div class="who"><i></i><div><b>Strider Sports</b><small>@StriderSport &nbsp;6 Aug 2015</small></div></div>
    <p>Win a Strider football pack consisting of everything you see below!</p>
    <div class="promo" role="img" aria-label="Promotional graphic for a football kit giveaway"></div>
  </div>
  <div class="scroll"><i></i></div>
</section>

<div class="abs sponsor" role="img" aria-label="Sponsor advert with an athlete running"></div>

<footer class="abs footer">
  <div class="mark">Marrowfield<br>Rovers FC</div>
  <h3 style="left:160px">CONTACT US</h3>
  <div class="addr">Marrowfield Rovers FC<br>Ashgrove Park, Millbrook Road, Fernhill<br>Carrowmore Co. Westmeath.</div>
  <div class="mail">
    <svg width="14" height="10" viewBox="0 0 14 10" fill="none" stroke="#fff" stroke-width="1"><rect x=".5" y=".5" width="13" height="9"/><path d="M.5 .5 7 6 13.5 .5"/></svg>
    <div>Email:<br>hello@marrowfieldrovers.com</div>
  </div>
  <h3 style="left:344px">OUR LOCATION</h3>
  <div class="map" role="img" aria-label="Street map showing the club grounds"></div>
  <h3 style="left:576px">QUICK LINKS</h3>
  <ul>
    <li>Home</li><li>About Us</li><li>Club Calendar</li><li>News</li><li>Location</li><li>Contact Us</li>
  </ul>
</footer>

<div class="abs copy">2016 © Marrowfield Rovers FC.All Rights Reserved</div>

</body>
</html>
```